チラシに使用する文章と画像はこちらで用意いたします。
全体の雰囲気はimageBのような感じです。
作りたいチラシのイメージはimageAのとおりです。
デザインは自由に調整いただいてかまいません。
使用する色はimageBのような「黒、茶」を考えておりますが、自由に調整いただいて結構です。

使用する文章はPDFファイルを参照下さい。
imageAのAからIはPDFの文章を入れて下さい。

imageAのDにいれる画像は「health.zip」をご使用下さい。
imageAのEにいれる画像は「urinary organs.zip」をご使用下さい。
imageAのFにいれる画像は「digestive organs.zip」をご使用下さい。
画像はimageBのように並べて下さい。

またimageAのD、E、Fのハーブの画像の上に「ORU・PLANTIVA」のマークを入れて下さい。
詳しくはimageAをご参照ください。
マークの画像はimageCをお使い下さい。
有機農作物はマークがないため、有機農作物と記載して下さい。
A4
片面
黒 茶色
• 高解像度JPG (.jpg)
• イラストレーター形式 (.ai)

柔らかい雰囲気やデザインなどとても気に入りました。
色合いも落ち着いているので、読みやすかったです。

たくさん提案くださり、誠にありがとうございます。
また機会があれば、どうぞよろしくお願い致します。

```html
<!DOCTYPE html>
<html lang="ja">
<head>
<meta charset="utf-8">
<title>ハーブ チラシ</title>
<link rel="stylesheet" href="https://fonts.googleapis.com/css2?family=Noto+Serif+JP:wght@500;700&family=Noto+Sans+JP:wght@400;500;700&display=swap">
<style>
:root{
  --paper:#f6efe2;
  --ink:#3b2d22;
  --brown:#7b5a3e;
  --brown-soft:#a88a6a;
  --olive:#8e9470;
  --olive-dark:#6d7352;
  --leaf:#7f9a54;
  --line:#c9b69b;
}
*{margin:0;padding:0;box-sizing:border-box}
html,body{width:849px;height:1200px;overflow:hidden;background:var(--paper)}
body{position:relative;font-family:"Noto Sans JP",sans-serif;color:var(--ink)}
.headline{position:absolute;left:50px;top:30px;font-family:"Noto Serif JP",serif;font-weight:700;color:var(--ink)}
.headline .line1{font-size:34px;letter-spacing:2px;display:flex;align-items:center}
.headline .line2{font-size:34px;letter-spacing:2px;margin-top:18px;margin-left:12px}
.accent{display:inline-block;margin-left:14px;padding:4px 18px;border:2px solid var(--brown);border-radius:50%;color:var(--brown);font-size:30px;transform:translateY(-14px)}
.dog-art{position:absolute;right:20px;top:14px;width:150px;height:190px;border-radius:40% 40% 30% 30%;background:radial-gradient(ellipse at 50% 40%,#d9c2a2,#b99671 70%,rgba(185,150,113,0) 72%);opacity:.85}

.intro{position:absolute;left:48px;top:232px;width:362px;background:var(--brown);color:#fff;padding:18px 20px 20px}
.intro h2{font-family:"Noto Serif JP",serif;font-size:21px;line-height:1.5;border-bottom:1px solid rgba(255,255,255,.5);padding-bottom:10px;margin-bottom:10px}
.intro p{font-size:11.5px;line-height:1.85}
.topic{position:absolute;left:48px;width:362px}
.topic h3{font-family:"Noto Serif JP",serif;font-size:17px;color:var(--brown);border-bottom:1px solid var(--line);padding-bottom:5px;margin-bottom:8px}
.topic p{font-size:11.5px;line-height:1.85}
.marks{position:absolute;left:48px;top:920px;width:362px;font-size:11px;line-height:1.7}
.marks li{list-style:none;margin-bottom:10px}
.marks .label{display:flex;align-items:center;gap:8px;font-weight:700;font-size:12.5px;color:var(--brown)}
.marks .badge{width:18px;height:18px;border-radius:50%;background:var(--leaf)}
.marks .badge.sq{border-radius:3px;background:var(--olive-dark)}
.marks .badge.tan{background:var(--brown-soft)}

.herb-set{position:absolute;left:453px;width:376px}
.herb-set h3{width:254px;background:var(--olive);color:#fff;font-family:"Noto Serif JP",serif;font-size:16px;text-align:center;padding:5px 0;border-radius:2px}
.price{width:254px;text-align:center;font-size:13px;font-weight:700;margin:5px 0 6px}
.grid{display:grid;grid-template-columns:repeat(3,78px);column-gap:10px;row-gap:6px;width:254px}
.herb{text-align:center}
.herb .photo{position:relative;width:78px;height:78px;border-radius:50%}
.herb .tag{position:absolute;left:-4px;top:-2px;background:var(--leaf);color:#fff;font-size:8px;padding:1px 4px;border-radius:2px}
.herb .tag.pl{background:var(--olive-dark)}
.herb span{display:block;font-size:9.5px;margin-top:2px;white-space:nowrap}
.herb-note{position:absolute;left:262px;top:0;width:114px;font-size:10.5px;line-height:1.75}
</style>
</head>
<body>

<header class="headline">
  <div class="line1">大切な家族だから、<span class="accent">いつまでも</span></div>
  <div class="line2">若々しく元気にいてほしい</div>
</header>
<div class="dog-art" role="img" aria-label="寄り添う犬のやわらかなイラスト"></div>

<section class="intro">
  <h2>現代の犬・猫にこそ<br>ハーブをおすすめします。</h2>
  <p>犬や猫が野生の肉食獣だった頃、獲物の内臓を一緒に食べていたと言います。草食動物の胃には消化された植物が入っていたからです。現代の生活ではその機会がなくなり、植物の恵みを取り入れる食事が大切になっています。</p>
</section>

<section class="topic" style="top:500px">
  <h3>特筆すべき抗酸化作用</h3>
  <p>「酸化」は、老化や様々な不調の原因です。ハーブには抗酸化物質が豊富に含まれ、体の内側から健やかさを保つお手伝いをします。毎日の食事に少し加えるだけで、無理なく続けられます。</p>
</section>

<section class="topic" style="top:690px">
  <h3>腸内環境を整える</h3>
  <p>腸は免疫細胞が多く集まる大切な場所です。ハーブに含まれる食物繊維や苦味成分は、腸内の環境を整え、消化を助けます。ペットの体調に合わせて選べるよう、三つの目的別ブレンドをご用意しました。</p>
</section>

<ul class="marks">
  <li><div class="label"><i class="badge"></i>有機ハーブ（有機ORUマーク）</div>第三者機関の認証を受けた、有機栽培のハーブです。</li>
  <li><div class="label"><i class="badge sq"></i>農薬不使用ハーブ（PLANTIVA）</div>農薬を使わずに育てられた、安心のハーブです。</li>
  <li><div class="label"><i class="badge tan"></i>有機農作物</div>有機農法で栽培された農作物を使用しています。</li>
</ul>

<section class="herb-set" style="top:255px">
  <h3>健康増進応援ハーブ</h3>
  <p class="price">25g入り 1260円</p>
  <div class="grid">
    <div class="herb"><div class="photo" role="img" aria-label="乾燥したバーチリーフ" style="background:radial-gradient(#8f8a55,#6d6a3c)"><i class="tag">ORU</i></div><span>バーチリーフ</span></div>
    <div class="herb"><div class="photo" role="img" aria-label="乾燥したダンデライオンリーフ" style="background:radial-gradient(#7c8650,#5d6838)"><i class="tag pl">PLANTIVA</i></div><span>ダンデライオンリーフ</span></div>
    <div class="herb"><div class="photo" role="img" aria-label="乾燥したネトル" style="background:radial-gradient(#76864c,#55663a)"><i class="tag">ORU</i></div><span>ネトル</span></div>
    <div class="herb"><div class="photo" role="img" aria-label="刻んだダンデライオンルート" style="background:radial-gradient(#b99a72,#8d6d4b)"><i class="tag pl">PLANTIVA</i></div><span>ダンデライオンルート</span></div>
    <div class="herb"><div class="photo" role="img" aria-label="乾燥したカモミール" style="background:radial-gradient(#d8c98e,#a99a5e)"><i class="tag">ORU</i></div><span>カモミール</span></div>
    <div class="herb"><div class="photo" role="img" aria-label="乾燥したヤロウ" style="background:radial-gradient(#9b9a6a,#737248)"><i class="tag pl">PLANTIVA</i></div><span>ヤロウ</span></div>
  </div>
  <p class="herb-note">毎日の食卓にそっと加えて、体の内側から元気をサポート。ビタミンやミネラルを多く含むハーブを、バランスよくブレンドしました。年齢を重ねた子にもおすすめです。</p>
</section>

<section class="herb-set" style="top:523px">
  <h3>泌尿器系応援ハーブ</h3>
  <p class="price">25g入り 1260円</p>
  <div class="grid">
    <div class="herb"><div class="photo" role="img" aria-label="乾燥したダンデライオンリーフ" style="background:radial-gradient(#7c8650,#5d6838)"><i class="tag">ORU</i></div><span>ダンデライオンリーフ</span></div>
    <div class="herb"><div class="photo" role="img" aria-label="乾燥したヤロウ" style="background:radial-gradient(#9b9a6a,#737248)"><i class="tag pl">PLANTIVA</i></div><span>ヤロウ</span></div>
    <div class="herb"><div class="photo" role="img" aria-label="乾燥したホーステール" style="background:radial-gradient(#8c9a62,#66743f)"><i class="tag">ORU</i></div><span>ホーステール</span></div>
    <div class="herb"><div class="photo" role="img" aria-label="乾燥したネトル" style="background:radial-gradient(#76864c,#55663a)"><i class="tag pl">PLANTIVA</i></div><span>ネトル</span></div>
    <div class="herb"><div class="photo" role="img" aria-label="乾燥したマシュマロウ" style="background:radial-gradient(#cdbb97,#a28d68)"><i class="tag">ORU</i></div><span>マシュマロウ</span></div>
    <div class="herb"><div class="photo" role="img" aria-label="乾燥したローズヒップ" style="background:radial-gradient(#b0553c,#7d3526)"><i class="tag pl">PLANTIVA</i></div><span>ローズヒップ</span></div>
  </div>
  <p class="herb-note">水分の少ない食事が続くと、泌尿器に負担がかかりがちです。巡りをやさしく整えるハーブを集めました。お水をしっかり飲む習慣とあわせてどうぞ。</p>
</section>

<section class="herb-set" style="top:787px">
  <h3>消化器系応援ハーブ</h3>
  <p class="price">25g入り 1260円</p>
  <div class="grid">
    <div class="herb"><div class="photo" role="img" aria-label="乾燥したネトル" style="background:radial-gradient(#76864c,#55663a)"><i class="tag">ORU</i></div><span>ネトル</span></div>
    <div class="herb"><div class="photo" role="img" aria-label="乾燥したダンデライオンリーフ" style="background:radial-gradient(#7c8650,#5d6838)"><i class="tag pl">PLANTIVA</i></div><span>ダンデライオンリーフ</span></div>
    <div class="herb"><div class="photo" role="img" aria-label="乾燥したカレンデュラ" style="background:radial-gradient(#e0a447,#b37a2c)"><i class="tag">ORU</i></div><span>カレンデュラ</span></div>
    <div class="herb"><div class="photo" role="img" aria-label="乾燥したマシュマロウ" style="background:radial-gradient(#e2d7bb,#b8a985)"><i class="tag pl">PLANTIVA</i></div><span>マシュマロウ</span></div>
    <div class="herb"><div class="photo" role="img" aria-label="乾燥したパパイヤ" style="background:radial-gradient(#c99a4f,#94692f)"><i class="tag">ORU</i></div><span>パパイヤ</span></div>
    <div class="herb"><div class="photo" role="img" aria-label="乾燥したペパーミント" style="background:radial-gradient(#6f8a4a,#4d6432)"><i class="tag pl">PLANTIVA</i></div><span>ペパーミント</span></div>
  </div>
  <p class="herb-note">下痢や便秘、食欲などお腹のトラブルを抱える子に。消化を助け、腸内環境を整えるハーブをブレンドしました。毎日の便の様子を見ながら、量を調整してください。</p>
</section>

</body>
</html>
```